JesterVolt Balloon Logo and Product Packaging Design

I need a package design for twisting balloons for my website jestervoltfun.com. The brand name that we will use is "jestervolt". The packaging will be 40cm long x 15 cm width with a see thru front and a top that can tear off. We can only use 3 colors max, but two colors would be better. We also will need a logo for "jestervolt". I have included our mockup front and back, our competitors packaging and our style guide. You can use our style guide and our mockups for inspiration but you please don't follow it exactly. You can also ignore them all together. Thanks, Corin

```html
<!DOCTYPE html>
<html lang="en">
<head>
<meta charset="utf-8">
<title>JesterVolt Balloon Packaging</title>
<link href="https://fonts.googleapis.com/css2?family=Ubuntu:wght@400;500&family=Ubuntu+Condensed&display=swap" rel="stylesheet">
<style>
  :root {
    --stage-grey: #808080;
    --pack-red: #ff0d0d;
    --window-slate: #435156;
    --strip-slate: #444f55;
    --paper-white: #ffffff;
    --balloon-sky: #8fe3ef;
    --balloon-mint: #cfeee6;
    --balloon-pink: #f2556a;
    --twist-red: #e8102a;
    --twist-rose: #ff5b78;
  }
  html, body {
    margin: 0;
    padding: 0;
    overflow: hidden;
  }
  .canvas {
    position: relative;
    width: 848px;
    height: 1200px;
    background: var(--stage-grey);
    overflow: hidden;
    font-family: "Ubuntu Condensed", "Ubuntu", sans-serif;
    color: var(--paper-white);
  }
  .brand-name {
    position: absolute;
    left: 0;
    width: 100%;
    text-align: center;
    font-family: "Ubuntu", sans-serif;
    font-weight: 400;
    color: var(--paper-white);
    margin: 0;
    line-height: 1;
  }
  .brand-tagline {
    position: absolute;
    left: 0;
    width: 100%;
    text-align: center;
    font-family: "Ubuntu", sans-serif;
    color: var(--paper-white);
    margin: 0;
    line-height: 1;
  }
  .hero .brand-name { top: 84px; font-size: 104px; letter-spacing: -1px; }
  .hero .brand-tagline { top: 192px; font-size: 37px; }

  .pack {
    position: absolute;
    top: 296px;
    height: 809px;
    width: 303px;
    box-shadow: 3px 3px 6px rgba(0,0,0,0.35);
    overflow: hidden;
  }
  .pack-front { left: 105px; background: var(--strip-slate); }
  .pack-back { left: 440px; background: var(--pack-red); }

  .front-header {
    position: absolute;
    top: 15px; left: 0;
    width: 100%; height: 141px;
    background: var(--pack-red);
  }
  .front-header .brand-name { top: 57px; font-size: 42px; }
  .front-header .brand-tagline { top: 107px; font-size: 19px; }

  .front-window {
    position: absolute;
    top: 156px; left: 0;
    width: 100%; height: 530px;
    background: var(--window-slate);
  }
  .balloon-cluster, .balloon-swan {
    position: absolute;
    display: block;
  }
  .balloon-cluster { left: 0; top: -18px; }
  .balloon-swan { left: 165px; top: 335px; }
  .piece-count {
    position: absolute;
    left: 25px; top: 488px;
    font-family: "Ubuntu Condensed", sans-serif;
    font-size: 34px;
    color: var(--pack-red);
    margin: 0;
  }
  .piece-count small { font-size: 24px; }

  .front-warning {
    position: absolute;
    top: 686px; left: 0;
    width: 100%; height: 109px;
    background: var(--pack-red);
  }
  .warning-title {
    position: absolute;
    left: 26px; top: 18px;
    margin: 0;
    display: flex;
    align-items: center;
    gap: 8px;
    font-size: 13px;
    font-weight: 400;
  }
  .warning-title b { font-weight: 400; font-family: "Ubuntu", sans-serif; font-weight: 500; font-size: 11.5px; }
  .warning-body {
    position: absolute;
    left: 26px; top: 45px;
    width: 262px;
    margin: 0;
    font-family: "Ubuntu", sans-serif;
    font-size: 7.4px;
    line-height: 10.2px;
  }

  .tear-line {
    position: absolute;
    top: 37px; left: 0;
    width: 100%;
    display: block;
  }
  .pack-back .brand-name { top: 88px; font-size: 42px; }
  .pack-back .brand-tagline { top: 140px; font-size: 19px; }

  .back-copy {
    position: absolute;
    left: 38px; top: 192px;
    width: 225px;
    font-family: "Ubuntu Condensed", sans-serif;
    font-size: 6.3px;
    line-height: 8.5px;
    text-align: justify;
  }
  .back-copy p { margin: 0 0 8px; }

  .latex-notice {
    position: absolute;
    left: 40px; top: 424px;
    width: 219px; height: 79px;
    border: 2px solid var(--paper-white);
    border-radius: 5px;
    box-sizing: border-box;
  }
  .latex-notice .notice-icon { position: absolute; left: 33px; top: 16px; }
  .latex-notice .notice-head {
    position: absolute; left: 76px; top: 13px;
    margin: 0; font-size: 16px;
  }
  .latex-notice .notice-line {
    position: absolute; left: 0; width: 100%; text-align: center;
    margin: 0; font-size: 12.5px;
  }
  .latex-notice .line-one { top: 35px; left: 16px; }
  .latex-notice .line-two { top: 52px; }

  .disposal-icons {
    position: absolute;
    left: 112px; top: 527px;
    display: flex; gap: 13px;
  }

  .origin-weight {
    position: absolute;
    left: 38px; top: 587px;
    display: flex; gap: 43px;
    font-size: 10.5px;
    margin: 0;
  }
  .maker-name {
    position: absolute;
    left: 38px; top: 690px;
    margin: 0;
    font-family: "Ubuntu", sans-serif;
    font-weight: 500;
    font-size: 26px;
  }
  .maker-site {
    position: absolute;
    left: 38px; top: 727px;
    margin: 0;
    font-family: "Ubuntu", sans-serif;
    font-size: 13.5px;
  }
  .maker-town {
    position: absolute;
    left: 38px; top: 747px;
    margin: 0;
    font-family: "Ubuntu", sans-serif;
    font-size: 9.5px;
  }
</style>
</head>
<body>
<main class="canvas">

  <header class="hero">
    <h1 class="brand-name">jestervolt</h1>
    <p class="brand-tagline">high-quality latex balloons</p>
  </header>

  <section class="pack pack-front" aria-label="Front of balloon pack">
    <div class="front-header">
      <h2 class="brand-name">jestervolt</h2>
      <p class="brand-tagline">high-quality latex balloons</p>
    </div>

    <div class="front-window">
      <svg class="balloon-cluster" width="190" height="370" viewBox="0 0 190 370" role="img" aria-label="Illustration of sky blue, mint striped and pink balloons with a red balloon-animal flower">
        <defs>
          <radialGradient id="clusterTone" cx="0.35" cy="0.4" r="0.8">
            <stop offset="0" stop-color="var(--balloon-mint)"/>
            <stop offset="0.45" stop-color="var(--balloon-sky)"/>
            <stop offset="1" stop-color="var(--balloon-pink)"/>
          </radialGradient>
        </defs>
        <rect x="0" y="0" width="130" height="365" rx="60" fill="url(#clusterTone)" opacity="0.9"/>
        <ellipse cx="110" cy="115" rx="68" ry="58" fill="var(--twist-red)" opacity="0.85"/>
      </svg>
      <svg class="balloon-swan" width="140" height="205" viewBox="0 0 140 205" role="img" aria-label="Illustration of a red balloon-animal swan">
        <defs>
          <linearGradient id="swanTone" x1="0" y1="0" x2="1" y2="1">
            <stop offset="0" stop-color="var(--twist-red)"/>
            <stop offset="1" stop-color="var(--twist-rose)"/>
          </linearGradient>
        </defs>
        <rect x="0" y="0" width="140" height="205" rx="30" fill="url(#swanTone)"/>
      </svg>
      <p class="piece-count">100 <small>PCS</small></p>
    </div>

    <div class="front-warning">
      <h3 class="warning-title">
        <svg width="22" height="20" viewBox="0 0 22 20" aria-hidden="true">
          <path d="M11 1 L21 19 H1 Z" fill="var(--paper-white)"/>
          <rect x="10" y="7" width="2" height="7" fill="var(--pack-red)"/>
          <rect x="10" y="15.5" width="2" height="2" fill="var(--pack-red)"/>
        </svg>
        <span><b>WARNING</b> : CHOKING HAZARD</span>
      </h3>
      <p class="warning-body">Children under eight (8) years old can choke or suffocate on uninflated or broken balloons. Adult supervision is required. Keep uninflated balloons from reach of children. Discard broken balloons responsibly.</p>
    </div>
  </section>

  <section class="pack pack-back" aria-label="Back of balloon pack">
    <svg class="tear-line" width="303" height="14" viewBox="0 0 303 14" aria-hidden="true">
      <line x1="0" y1="7" x2="303" y2="7" stroke="var(--paper-white)" stroke-width="1" stroke-dasharray="7 5"/>
      <g stroke="var(--paper-white)" stroke-width="1.3" fill="none">
        <circle cx="262" cy="3" r="2.6"/>
        <circle cx="262" cy="11" r="2.6"/>
        <line x1="264" y1="4.5" x2="276" y2="10"/>
        <line x1="264" y1="9.5" x2="276" y2="4"/>
      </g>
    </svg>

    <h2 class="brand-name">jestervolt</h2>
    <p class="brand-tagline">high-quality latex balloons</p>

    <div class="back-copy">
      <p>Our twisting balloons are made for clowns, party hosts and hobby artists who need colour, stretch and strength in every pull. Each balloon is dipped, dried and checked by hand so it twists cleanly, holds its shape and pops far less often than cheaper brands. Inflate with a hand pump to about three quarters and leave a short tail at the end. Keep the pack sealed and away from heat and sunlight to keep the latex soft and bright for longer. Tie off with a firm knot before you start shaping any figure.</p>
      <p>Start with simple shapes such as dogs, swords and flowers, then move on to swans, hats and larger sculptures as your hands learn the feel of the latex. Always twist in the same direction and lock each bubble before adding the next one. Slight warmth from your palms makes the balloon easier to bend. Work on a clean table and brush away any grit that could cause a pop. Store leftover balloons in a cool drawer, and never leave loose pieces where small children can reach them. Enjoy the show.</p>
    </div>

    <div class="latex-notice">
      <svg class="notice-icon" width="32" height="29" viewBox="0 0 32 29" aria-hidden="true">
        <path d="M16 1 L31 28 H1 Z" fill="var(--paper-white)"/>
        <rect x="14.5" y="10" width="3" height="10" fill="var(--pack-red)"/>
        <rect x="14.5" y="22" width="3" height="3" fill="var(--pack-red)"/>
      </svg>
      <p class="notice-head">MADE OF 100%</p>
      <p class="notice-line line-one">Natural Rubber Latex</p>
      <p class="notice-line line-two">Which May Cause Allergic Reactions</p>
    </div>

    <div class="disposal-icons" aria-label="Disposal and safety marks">
      <svg width="28" height="28" viewBox="0 0 28 28" aria-hidden="true">
        <circle cx="18" cy="5" r="3" fill="var(--paper-white)"/>
        <path d="M18 9 L18 20 L21 27 M18 14 L12 16" stroke="var(--paper-white)" stroke-width="2.5" fill="none"/>
        <path d="M4 17 H13 L11.5 27 H5.5 Z" fill="var(--paper-white)"/>
      </svg>
      <svg width="28" height="28" viewBox="0 0 28 28" aria-hidden="true">
        <circle cx="14" cy="14" r="12" stroke="var(--paper-white)" stroke-width="2" fill="none"/>
        <line x1="5.5" y1="5.5" x2="22.5" y2="22.5" stroke="var(--paper-white)" stroke-width="2"/>
      </svg>
      <svg width="28" height="28" viewBox="0 0 28 28" aria-hidden="true">
        <path d="M14 3 L26 24 H2 Z" stroke="var(--paper-white)" stroke-width="2.5" fill="none"/>
      </svg>
      <svg width="28" height="28" viewBox="0 0 28 28" aria-hidden="true">
        <rect x="3" y="5" width="22" height="18" rx="3" fill="var(--paper-white)"/>
      </svg>
    </div>

    <p class="origin-weight"><span>Made In China</span><span>Net Wt. 25g</span></p>

    <p class="maker-name">JesterVolt Fun</p>
    <p class="maker-site">www.jestervoltfun.com</p>
    <p class="maker-town">Millbrook, Vermont</p>
  </section>

</main>
</body>
</html>
```